Harborline Crest Insurance Services

we are a high end insurance agency we specialize on Auto | Home | Business | Life looking for something professional and luxuries at the same time. if you guys need anything else please let me know.

Auto | Home | Business | Life must be under logo on the back with black background.

i want the back part to be black with our gold logo on it.

Target Market(s)

Auto | Home | Business | Life

Industry/Entity Type

Insurance Broker

Contact Information for Business Card

My logo is gold so a black in the back would be nice.

Font styles to use
Serif

Colors
000000

Requirements
Must have
• Big logo on the back with black background.

```html
<!DOCTYPE html>
<html lang="en">
<head>
<meta charset="utf-8">
<title>Harborline Crest Insurance Services – Business Card</title>
<link rel="stylesheet" href="https://fonts.googleapis.com/css2?family=Cinzel:wght@600&family=Montserrat:wght@500;700&family=Noto+Serif:wght@400&display=swap">
<style>
  :root {
    --ink: #000000;
    --paper: #ffffff;
    --gold: #e9b42a;
    --line: #111111;
  }
  * { box-sizing: border-box; margin: 0; padding: 0; }
  html, body { width: 1200px; height: 1200px; overflow: hidden; background: var(--paper); }
  .sheet {
    position: relative; width: 1200px; height: 1200px;
    display: flex; align-items: center; justify-content: center; gap: 36px;
  }
  .card {
    position: relative; width: 540px; height: 340px;
    border-radius: 30px; overflow: hidden;
  }
  /* Front */
  .card--front { background: var(--ink); border: 2px solid var(--line); }
  .front__top {
    position: absolute; left: 0; top: 0; right: 0; height: 98px;
    background: var(--paper);
  }
  .front__name {
    position: absolute; right: 62px; top: 28px;
    font: 700 19px "Montserrat", sans-serif; letter-spacing: 0.5px; color: var(--ink);
  }
  .front__band {
    position: absolute; left: 0; right: 0; top: 98px; height: 142px;
    display: flex; align-items: center; justify-content: center; gap: 16px;
  }
  .brand__dot { width: 46px; height: 46px; border-radius: 50%; background: var(--gold); flex: none; }
  .brand__name {
    font: 600 27px/1.05 "Cinzel", serif; color: var(--gold);
  }
  .brand__name span { display: block; font-size: 13px; letter-spacing: 4px; margin-top: 6px; }
  .front__contacts {
    position: absolute; left: 0; right: 0; top: 240px; height: 68px;
    background: var(--paper);
    display: flex; align-items: center; justify-content: space-around; padding: 0 18px;
  }
  .contact {
    display: flex; align-items: center; gap: 5px;
    font: 500 15px "Montserrat", sans-serif; color: var(--ink);
  }
  .contact svg { width: 14px; height: 14px; flex: none; }
  /* Back */
  .card--back {
    background: var(--ink);
    display: flex; flex-direction: column; align-items: center; justify-content: center;
  }
  .back__brand { display: flex; flex-direction: column; align-items: center; gap: 18px; }
  .back__brand .brand__dot { width: 110px; height: 110px; }
  .back__brand .brand__name { font-size: 30px; text-align: center; }
  .back__brand .brand__name span { font-size: 13px; letter-spacing: 4.5px; }
  .services {
    margin-top: 26px;
    font: 400 19px "Noto Serif", serif; color: var(--paper); letter-spacing: 0.3px;
  }
  .services .sep { margin: 0 8px; }
</style>
</head>
<body>
<main class="sheet">
  <section class="card card--front" aria-label="Card front">
    <div class="front__top"><p class="front__name">NAME</p></div>
    <div class="front__band">
      <span class="brand__dot"></span>
      <p class="brand__name">Harborline Crest<span>INSURANCE SERVICES</span></p>
    </div>
    <div class="front__contacts">
      <p class="contact">
        <svg viewBox="0 0 16 16" aria-hidden="true"><rect x="1" y="3" width="14" height="10" fill="#000"/><path d="M1 3l7 6 7-6" fill="none" stroke="#fff" stroke-width="1.3"/></svg>
        harborlinecrest
      </p>
      <p class="contact">
        <svg viewBox="0 0 16 16" aria-hidden="true"><circle cx="8" cy="8" r="6" fill="#000"/></svg>
        harborlinecrest
      </p>
      <p class="contact">
        <svg viewBox="0 0 16 16" aria-hidden="true"><path d="M8 1a5 5 0 0 1 5 5c0 4-5 9-5 9S3 10 3 6a5 5 0 0 1 5-5z" fill="#000"/><circle cx="8" cy="6" r="1.8" fill="#fff"/></svg>
        harborlinecrest
      </p>
    </div>
  </section>

  <section class="card card--back" aria-label="Card back">
    <div class="back__brand">
      <span class="brand__dot"></span>
      <p class="brand__name">Harborline Crest<span>INSURANCE SERVICES</span></p>
    </div>
    <p class="services">Auto<span class="sep">|</span>Home<span class="sep">|</span>Business<span class="sep">|</span>Life</p>
  </section>
</main>
</body>
</html>
```